Book Cover for a book on Quiet Ledgers

I am self-publishing my book on Bookvale and need a book cover made. Below are the details. See attached templates for size we need to use. I also attached a previous cover we had made that I liked. The problem with it was they were two boys helping each other but the book is about women. I'm open to your ideas on the cover though, but I wanted to show you a style I liked as an idea.
Front of Cover
Book Title: Quiet Ledgers
Book Subtitle: Morning Letters of a Harbor Keeper
Author Name: Lorna T. Beckett
Add on the Spine of Cover: Quiet Ledgers and Lorna T. Beckett
Back of the Cover Text:
Quiet Ledgers: Morning Letters of a Harbor Keeper is an honest account of a business owner’s experience attempting to navigate the start-up community while also pursuing spiritual growth. Author Lorna Beckett defines a spiritual entrepreneur as “someone who runs an enterprise with the purpose of growing love rather than material gain.” This book discusses the three dimensions of Quiet Ledgers:
1. The business is an integral part of the founder’s spiritual journey.
2. Employees working for the spiritual enterprise, whether they know it or not, encounter this company because it's part of their spiritual path.
3. The business itself has a life force of its own and its purpose is to further the kingdom of heaven on earth.
These three dimensions happen simultaneously and work together to produce the greatest possible result. However, this can feel confusing to a founder juggling these dimensions while also trying to manage and run a business. This is not a formulaic self-help book or roadmap. Rather, it is a compilation of personal reflections that often seem at odds with the traditional world of entrepreneurship.
Below the description add my picture (see attached for my picture)
Bio text:
Lorna Beckett founded Tellway with the vision of ushering in a life-long education system that shifts away from standardization to one that empowers people to live their purpose. In college, Lorna interned for Bright Lanterns, a women’s empowerment initiative where she recognized her passion for helping people find their voice. Lorna's 20-year journey has come full circle to empowering other female CEOs who are pursuing the path of Quiet Ledgers.
NOTE: Please note that Bookvale puts a bar code on the bottom right of the back cover as is noted on the attached template.
Size template is attached to the brief, here are the sizes typed out:
# Description Width (in) Height (in)
1 Full Cover 12.79 9.25
2 Front Cover 6 9
3 Safe Area 5.875 8.75
4 Bleed 0.125 0.125
5 Margin 0.125 0.125
6 Spine 0.54 9
7 Spine Safe Area 0.415 8.75
8 Spine Margin 0.062 0.062
9 Barcode Margin 0.25 0.25
Pre-publication checklist
BOOKVALE TIPS for the final cover:
1. Save as a PDF. Your cover must be a single PDF that includes the back cover, spine, and front cover as one image.
2. Flatten all transparencies. These can cause the file to print with missing or distorted content. Consult your software's documentation to learn how.
3. Embed your fonts. Consult your software's documentation to learn how.
4. Remove crop marks, color bars, template text. Crop marks are lines showing where pages should be trimmed. Color bars are strips with a series of patches used to ensure color balance during printing. Also, remove any template text, PDF creation guides, or software references.
5. Ensure your cover image meets the minimum resolution of 300 DPI (dots per inch).
6. Optimize PDFs. Optimization is useful to reduce your file size, allowing for higher performance when transferring, uploading, viewing, and printing the files.
7. Remove file security. Locked or encrypted files will fail review.
Target Market(s)
Women who want to be CEOs or are currently CEOs of companies.
Industry/Entity Type
Entrepreneurship, business, spirituality
Requirements
Must have
- Just the text on the description. A very welcoming feel.
Nice to have
- I like the idea of having a sunrise/sunset in the image somehow like in the example I attached to the brief, but again I'm open.
Should not have
- Please don't put any yoga or meditation poses or hands outstretched. I have a lot of interesting ones that look like my example so if you are going to submit after Saturday 10/29, please only do so if you have a new idea! Thanks!

```html
<!DOCTYPE html>
<html lang="en">
<head>
<meta charset="utf-8">
<title>Quiet Ledgers – Book Cover</title>
<link rel="stylesheet" href="https://fonts.googleapis.com/css2?family=Allura&family=Oswald:wght@400;500&family=Marcellus&family=Libre+Caslon+Text&display=swap">
<style>
  :root {
    --sky-blue: #4f77ad;
    --sky-pale: #c9c6d2;
    --glow: #f2a468;
    --ember: #d9734a;
    --dusk: #6b4a4c;
    --ground: #231a1b;
    --ink-light: #ffffff;
    --ink-dark: #1f2a3b;
    --portrait: #a88a78;
  }
  * { box-sizing: border-box; margin: 0; padding: 0; }
  html, body { width: 1200px; height: 867px; overflow: hidden; background: var(--ground); }
  .cover { position: relative; width: 1200px; height: 867px; overflow: hidden; }
  .cover__scene { position: absolute; inset: 0; width: 100%; height: 100%; }

  .back {
    position: absolute; left: 55px; top: 52px; width: 472px;
    font-family: "Libre Caslon Text", Georgia, serif;
    font-size: 13.2px; line-height: 18.2px; color: var(--ink-light);
  }
  .back p { margin-bottom: 12px; }
  .dimensions { list-style: none; margin: -6px 0 12px; }
  .dimensions li { padding-left: 26px; position: relative; }
  .dimensions li::before { content: "✦"; position: absolute; left: 26px; transform: translateX(-100%); padding-right: 8px; font-size: 12px; }
  .dimensions li { text-indent: 14px; }
  .bio { position: absolute; left: 55px; top: 476px; width: 286px;
    font-family: "Libre Caslon Text", Georgia, serif; font-size: 13.2px; line-height: 18.2px; color: var(--ink-light); }
  .author-portrait { position: absolute; left: 358px; top: 478px; width: 175px; height: 226px; }

  .spine { position: absolute; left: 572px; top: 0; width: 40px; height: 867px; }
  .spine__title, .spine__author {
    position: absolute; left: 0; writing-mode: vertical-rl;
    font-family: "Oswald", sans-serif; font-weight: 500; font-size: 27px;
    letter-spacing: 0.5px; color: var(--ink-light); line-height: 40px;
  }
  .spine__title { top: 72px; }
  .spine__author { top: 556px; }

  .front { position: absolute; left: 625px; top: 0; width: 575px; height: 867px; text-align: center; }
  .front__script {
    position: absolute; left: 0; right: 0; top: 40px;
    font-family: "Allura", cursive; font-size: 190px; line-height: 1;
    color: var(--ink-light); opacity: 0.95;
  }
  .front__title {
    position: absolute; left: 0; right: 0; top: 232px;
    font-family: "Oswald", sans-serif; font-weight: 500; font-size: 72px;
    letter-spacing: 1px; color: var(--ink-light); line-height: 1;
  }
  .front__subtitle {
    position: absolute; left: 0; right: 0; top: 346px;
    font-family: "Marcellus", serif; font-size: 30px; color: var(--ink-dark);
  }
  .front__author {
    position: absolute; left: 0; right: 0; top: 765px;
    font-family: "Oswald", sans-serif; font-weight: 500; font-size: 62px;
    line-height: 1; color: var(--ink-light);
  }
</style>
</head>
<body>
<main class="cover">
  <svg class="cover__scene" viewBox="0 0 1200 867" preserveAspectRatio="none" role="img" aria-label="Sunset over mountain ridges with three women standing on a rocky outcrop in silhouette">
    <defs>
      <linearGradient id="sky" x1="0" y1="0" x2="0" y2="1">
        <stop offset="0" stop-color="var(--sky-blue)"/>
        <stop offset="0.28" stop-color="var(--sky-pale)"/>
        <stop offset="0.45" stop-color="var(--glow)"/>
        <stop offset="0.6" stop-color="var(--dusk)"/>
        <stop offset="0.78" stop-color="var(--ground)"/>
        <stop offset="1" stop-color="var(--ground)"/>
      </linearGradient>
      <radialGradient id="sun" cx="0.62" cy="0.47" r="0.45">
        <stop offset="0" stop-color="var(--ember)" stop-opacity="0.85"/>
        <stop offset="1" stop-color="var(--ember)" stop-opacity="0"/>
      </radialGradient>
      <linearGradient id="leftShade" x1="0" y1="0" x2="1" y2="0">
        <stop offset="0" stop-color="var(--ground)" stop-opacity="0.55"/>
        <stop offset="0.45" stop-color="var(--ground)" stop-opacity="0"/>
      </linearGradient>
    </defs>
    <rect width="1200" height="867" fill="url(#sky)"/>
    <rect width="1200" height="867" fill="url(#sun)"/>
    <rect width="1200" height="867" fill="url(#leftShade)"/>
  </svg>

  <section class="back">
    <p>Quiet Ledgers: Morning Letters of a Harbor Keeper is an honest account of a business owner’s experience attempting to navigate the start-up community while also pursuing spiritual growth. Author Lorna Beckett defines a spiritual entrepreneur as “someone who runs an enterprise with the purpose of growing love rather than material gain.” This book discusses the three dimensions of Quiet Ledgers:</p>
    <ul class="dimensions">
      <li>The business is an integral part of the founder’s spiritual journey.</li>
      <li>Employees working for the spiritual enterprise, whether they know it or not, encounter this company because it's part of their spiritual path.</li>
      <li>The business itself has a life force of its own and its purpose is to further the kingdom of heaven on earth.</li>
    </ul>
    <p>These three dimensions happen simultaneously and work together to produce the greatest possible result. However, this can feel confusing to a founder juggling these dimensions while also trying to manage and run a business. This is not a formulaic self-help book or roadmap. Rather, it is a compilation of personal reflections that often seem at odds with the traditional world of entrepreneurship.</p>
  </section>
  <p class="bio">Lorna Beckett founded Tellway with the vision of ushering in a life-long education system that shifts away from standardization to one that empowers people to live their purpose. In college, Lorna interned for Bright Lanterns, a women’s empowerment initiative where she recognized her passion for helping people find their voice. Lorna's 20-year journey has come full circle to empowering other female CEOs who are pursuing the path of Quiet Ledgers.</p>
  <svg class="author-portrait" viewBox="0 0 175 226" role="img" aria-label="Author portrait photograph">
    <defs>
      <linearGradient id="portraitTone" x1="0" y1="0" x2="0" y2="1">
        <stop offset="0" stop-color="#c9c7b4"/>
        <stop offset="0.5" stop-color="var(--portrait)"/>
        <stop offset="1" stop-color="#d04a5e"/>
      </linearGradient>
    </defs>
    <rect width="175" height="226" fill="url(#portraitTone)"/>
  </svg>

  <aside class="spine">
    <span class="spine__title">QUIET LEDGERS</span>
    <span class="spine__author">LORNA T. BECKETT</span>
  </aside>

  <section class="front">
    <div class="front__script">Quiet</div>
    <h1 class="front__title">LEDGERS</h1>
    <p class="front__subtitle">Morning Letters of a Harbor Keeper</p>
    <p class="front__author">LORNA T. BECKETT</p>
  </section>
</main>
</body>
</html>
```